Velorami.com - have media you dont own! Velorami the idols - Site Concept

VELORAMI those who ENTERTAIN you, who you LISTEN to, who you IDOLISE, and who you 'BORROW' from... VELORAMI the IDOLS the things that are the STARS... see brief concept at www.velorami-example.com

Looking for site concept, something new, very simple transaction, not generic website. Must also drive mobile app download call to action.

In principle, we dont care how you get your media or watch a TV series or download your favourite song, however, if you are honest and love the song/movie/servies or the star, pay them!
The solution should include anonymous/protected end user interaction and digital certificate/rights management process for end users who have media not paid for to velorami and receive an approved digital certificate from Velorami authorised by the relevant media house proving legal ownership of the digital media item (music, video, TV series/episode, movie etc...)

Basic functions:
Consumer: Mobile and Web
Personal media rights administration
1. Capture core data – Create secure and private Profile account
2. Log owned/borrowed media (media legally owned tagged and media 'borrowed' tagged, decision criteria, pledge or purchase (open to ideas, function to browse PC for media on HDD/Songbarrel or mobile, tag ones to pay for etc, capture CD's owned etc. create digital library filing system?)
3. Pledge payment for media - future payment value linked to market value, I like this, not sure I will keep it forever though, pay less? use once?
4. Purchase rights for media - payment based on market value of related media item. (quidlane, credit card or other?)
5. Media Certificate management - secure and PRIVATE distribution of the certificate (open to options here), approved by media house.

design ideas welcome, modern, fast, simple steps, engaging, with sense of privacy, we wont share data, we will just pay the media houses more! Based in Switzerland, managed by Swiss privacy law. transact with min personal data required.

Reason: The service committed to 50+ designs, most received are form one provider, all off the mark and very basic, not impressed so far, was expecting some real design thought rather than standard templates being rehashed, thats not deisgn? Hope in next days I am impressed?

Target Market(s)

Digital Media Consumer

Industry/Entity Type

Media

Number of Pages Required

5+ page

Font styles to use
Sans Serif

Requirements
Must have
• Must have privacy by design, must have simple and minimal steps taken to log and declare media items and pay, with no risk of exposure. Must have payment process, must have interface to easily load media into site, drag drop, search HDD/mobile etc.
Nice to have
• Digital certificate process and admin interaction of site and with media house, secure and trusted process to provide report and logs of payment for media to specific media house and relevant payments made and tracked.
Should not have
• complex workflows are out, complex payment methods.

```html
<!DOCTYPE html>
<html lang="en">
<head>
<meta charset="utf-8">
<title>Velorami – Have media you don't own</title>
<link href="https://fonts.googleapis.com/css2?family=Open+Sans:ital,wght@0,400;0,600;0,700;1,400&family=Oswald:wght@500;700&family=Libre+Baskerville:ital@1&display=swap" rel="stylesheet">
<style>
:root{
  --ink:#1e1e1e;
  --bar:#232323;
  --header:#2b2b2b;
  --blue:#2b8ef0;
  --blue-deep:#1f7fe0;
  --white:#ffffff;
  --muted:#bdbdbd;
  --grey-text:#6b6b6b;
  --footer:#2a2a2a;
  --footer-bottom:#1c1c1c;
}
*{margin:0;padding:0;box-sizing:border-box}
html,body{width:723px;height:1200px;overflow:hidden;background:var(--white)}
body{font-family:"Open Sans",Arial,sans-serif;color:var(--white);position:relative}

/* header */
.topbar{height:22px;background:var(--bar);display:flex;justify-content:space-between;align-items:center;padding:0 180px 0 190px;font-size:7px;color:var(--muted)}
.topbar span{margin-right:14px}
.mainbar{height:31px;background:var(--header);position:relative;text-align:center}
.brand{font-family:"Libre Baskerville",serif;font-style:italic;font-size:13px;color:var(--white);position:absolute;left:0;right:0;top:2px}
.nav{position:absolute;left:0;right:0;bottom:4px;display:flex;justify-content:center;gap:16px;font-size:7px;color:#d0d0d0}

/* hero */
.hero{height:237px;position:relative;text-align:center;background:radial-gradient(ellipse at 55% 40%,#9a9a9a 0%,#5a5a5a 40%,#262626 80%)}
.hero-photo{position:absolute;inset:0}
.hero-copy{position:relative;padding-top:62px;font-family:"Libre Baskerville",serif;font-style:italic;font-size:10.5px;line-height:15px;color:var(--white);width:330px;margin:0 auto}
.btn{display:inline-block;background:var(--blue);color:var(--white);font-size:7px;padding:5px 14px;font-family:"Open Sans",sans-serif;font-style:normal;border-radius:2px}
.hero .btn{margin-top:16px}
.dots{position:absolute;bottom:12px;left:0;right:0;display:flex;justify-content:center;gap:6px}
.dots i{width:5px;height:5px;border-radius:50%;background:#888}
.dots i.on{background:var(--white)}

/* welcome */
.welcome{height:145px;background:var(--blue);display:flex;align-items:center;padding:0 120px 0 188px}
.welcome h2{font-family:"Oswald",sans-serif;font-weight:700;font-size:21px;line-height:23px;width:130px}
.welcome .divider{width:1px;height:92px;background:rgba(255,255,255,.7);margin:0 26px 0 8px}
.welcome .text{font-size:6.5px;line-height:10px;width:200px}
.welcome .btn{background:var(--blue-deep);border:1px solid rgba(255,255,255,.6);margin-top:8px;padding:3px 10px}

/* services */
.services{height:205px;background:linear-gradient(180deg,#2a2a2a,#3d3d3d 55%,#1d1d1d);position:relative}
.services .lead{text-align:center;padding-top:14px;width:360px;margin:0 auto}
.services .lead h3{font-size:9.5px;font-weight:700;line-height:12px}
.services .lead p{font-size:6px;color:var(--muted);margin-top:5px;line-height:9px}
.services h2{position:absolute;left:188px;top:110px;font-family:"Oswald",sans-serif;font-weight:700;font-size:21px}
.service-list{position:absolute;left:320px;top:84px;list-style:none;font-size:6.5px;line-height:9px;width:220px}
.service-list li{margin-bottom:7px;padding-left:8px;position:relative}
.service-list li::before{content:"";position:absolute;left:0;top:3px;width:3px;height:3px;background:var(--white)}

/* app */
.app{height:240px;background:var(--white);text-align:center;color:var(--ink)}
.app h2{font-family:"Open Sans",sans-serif;font-weight:700;font-size:22px;padding-top:20px}
.app p{font-size:6px;color:var(--grey-text);width:250px;margin:4px auto 0;line-height:9px}
.app-row{display:flex;justify-content:center;align-items:flex-end;gap:14px;margin-top:14px}
.devices{width:190px;height:92px;background:linear-gradient(180deg,#3a8ee6,#1b5fb8);border-radius:4px}
.badges{display:flex;flex-direction:column;gap:8px;padding-bottom:10px}
.badge{width:58px;height:20px;border-radius:3px;background:#1a1a1a}
.badge.green{background:#7cb342}
.app .btn{margin-top:18px;padding:6px 14px}

/* quote */
.quote{height:112px;background:linear-gradient(90deg,#2c2c2c,#6a6a6a 50%,#3a3a3a);display:flex;align-items:center;justify-content:center}
.quote p{font-family:"Libre Baskerville",serif;font-style:italic;font-size:13px;line-height:19px;text-align:center;width:340px}

/* footer */
.footer{height:180px;background:var(--footer);display:flex;padding:20px 0 0 188px;gap:42px}
.footer h4{font-size:7.5px;font-weight:700;margin-bottom:8px}
.footer .field{width:120px;height:12px;background:var(--white);margin:3px 0 6px}
.footer label{font-size:6px;color:var(--muted)}
.footer .btn{padding:3px 40px}
.footer .line{font-size:6px;color:var(--muted);margin-bottom:5px}
.social{display:flex;gap:5px}
.social i{width:13px;height:13px;border-radius:50%;background:#4a4a4a}
.legal{position:absolute;left:0;right:0;bottom:0;height:20px;background:var(--footer-bottom);display:flex;align-items:center;justify-content:space-between;padding:0 12px 0 188px;font-size:5.5px;color:#8a8a8a}
.pay{display:flex;gap:3px}
.pay i{width:14px;height:9px;background:#3f5fa8;border-radius:1px}
.pay i:nth-child(2){background:#c9302c}
.pay i:nth-child(3){background:#e8a317}
.pay i:nth-child(4){background:#5b9bd5}
</style>
</head>
<body>
<header>
  <div class="topbar">
    <div><span>+41 00 000 00 00</span><span>hello@velorami-example.com</span></div>
    <div>Login</div>
  </div>
  <div class="mainbar">
    <div class="brand">Velorami</div>
    <nav class="nav"><span>Home</span><span>About</span><span>Services</span><span>Pledge</span><span>Contact</span></nav>
  </div>
</header>

<section class="hero">
  <div class="hero-photo" role="img" aria-label="Black and white close-up photo of headphones resting on a record"></div>
  <div class="hero-copy">
    VELORAMI those who ENTERTAIN you, who you LISTEN to, who you IDOLISE, and who you 'BORROW' from... VELORAMI the IDOLS
    <br><span class="btn">Learn More</span>
  </div>
  <div class="dots"><i class="on"></i><i></i></div>
</section>

<section class="welcome">
  <h2>WELCOME TO OUR SITE!</h2>
  <div class="divider"></div>
  <div>
    <p class="text">* * * A new way to honour the stars you love. Log the songs, films and series you enjoy, pledge or pay a fair share to the media houses, and receive a private certificate of ownership. No data shared, only paid forward to the people who made it.</p>
    <span class="btn">More</span>
  </div>
</section>

<section class="services">
  <div class="lead">
    <h3>VELORAMI your stars entrepreneurs and receive a digital certificate validating and legalizing your digital rights to the media you freely obtained or viewed online.</h3>
    <p>All personal data is kept private under Swiss law. To log your media and pay its creators, just follow a few simple steps through our secure platform.</p>
  </div>
  <h2>OUR SERVICES</h2>
  <ul class="service-list">
    <li>Capture core data – create a secure and private profile account</li>
    <li>Create digital library filing system</li>
    <li>Pledge payment for media – future payment linked to market value</li>
    <li>Purchase rights for media – payment based on market value</li>
    <li>Media Certificate management – secure and PRIVATE distribution of the certificate approved by media house</li>
  </ul>
</section>

<section class="app">
  <h2>Get Our APP</h2>
  <p>Log your media, pledge or pay in seconds and keep your certificates with you wherever you go. Download the app for tablet and phone.</p>
  <div class="app-row">
    <div class="devices" role="img" aria-label="Tablet and two phones showing the Velorami app screen"></div>
    <div class="badges"><div class="badge green"></div><div class="badge"></div><div class="badge"></div></div>
  </div>
  <span class="btn">DOWNLOAD</span>
</section>

<section class="quote" role="img" aria-label="Dim photo of a vintage radio and turntable">
  <p>Time to show respect, appreciation, honour and whatever, use VELORAMI</p>
</section>

<footer class="footer">
  <div>
    <h4>SIGNUP FOR UPDATES</h4>
    <label>Name</label><div class="field"></div>
    <label>Email</label><div class="field"></div>
    <span class="btn">SIGN UP</span>
  </div>
  <div>
    <h4>FIND US</h4>
    <p class="line">Telephone: +41 00 000 00 00</p>
    <p class="line">hello@velorami-example.com</p>
  </div>
  <div>
    <h4>KEEP IN TOUCH</h4>
    <div class="social"><i></i><i></i><i></i><i></i></div>
  </div>
</footer>
<div class="legal">
  <span>Copyright © Velorami. All rights reserved.</span>
  <div class="pay"><i></i><i></i><i></i><i></i></div>
</div>
</body>
</html>
```